KT Prime Motion personal training needs a new Business Card design for 2016

Business Card design:
Our current business card is very plain
We are bringing on our first team member next year and thought its a perfect time to have a new face lift for our company!

We are a Personal Training business "KT Prime Motion" who specializes in strength and conditioning / weightloss training,
We also run a yearly Bootcamp called "Ferocity Drillcamps", this is our Logo Design which we are looking for

The pink and blue in the logo are our business colours, how ever we don't want those colours to heavily dominate the card.

We are looking for a business card which is eye catching, and creative.

I am open to suggestions and any designs :)

Logo Design:

For our Logo Design we are looking for a bright, energetic logo, preferably a word logo which portrays strength and high intensity
If it has icon's etc in it thats fine again im open for suggestions :)
The Logo Design is for our Bootcamp which runs yearly
The bootcamp is called "Ferocity Drillcamp"

Target Market(s)

Age 20-40
Individuals who want to look great and have more energy

Industry/Entity Type

Business

Contact Information for Business Card

On the front
KT Prime Motion Doriel Maxton Personal Training / Bootcamps / Pilates / Nutrition Healthy mind, Healthy body, Ultimate lifestyle < our slogan
Icons for the following
Email:
Mobile:
plain square:
plain square:

On the back we would like to include somewhere
"Show this card to receive 50% off your first 30min pt session"
"Valid to one user only"

Logo Text

Ferocity Drillcamp

Font styles to use
Serif

Colors
e34197
0255a3
000000
ffffff

Requirements
Must have
• - Icons for instagram, facebook, email and mobile phone
• - Slogan: Healthy mind, Healthy body, Ultimate lifestyle
• - What we offer: Personal Training , Bootcamps, Pilates, Nutrition
• - Logo
• -
Nice to have
• - Our 50% offer on the back
• - a place for a photo
Should not have
• - Pink and Blue everywhere

```html
<!DOCTYPE html>
<html lang="en">
<head>
<meta charset="utf-8">
<title>KT Prime Motion – Business Card</title>
<link rel="stylesheet" href="https://fonts.googleapis.com/css2?family=Archivo:wght@600&family=Libre+Baskerville&display=swap">
<style>
  :root {
    --brand-blue: #0255a3;
    --brand-pink: #e34197;
    --ink: #333333;
    --paper: #ffffff;
    --edge: #cfcfcf;
  }
  html, body {
    margin: 0;
    padding: 0;
    width: 1200px;
    height: 677px;
    overflow: hidden;
    background: var(--paper);
  }
  .card {
    position: relative;
    width: 1200px;
    height: 677px;
    background: var(--paper);
    font-family: "Libre Baskerville", Georgia, serif;
    color: var(--ink);
  }
  .card-edge {
    position: absolute;
    left: 11px; top: 5px;
    width: 1181px; height: 672px;
    border: 1px solid var(--edge);
    box-sizing: border-box;
  }
  .owner-name {
    position: absolute;
    left: 0; right: 0; top: 56px;
    margin: 0;
    text-align: center;
    font-family: "Archivo", Arial, sans-serif;
    font-weight: 600;
    font-size: 80px;
    line-height: 1;
    letter-spacing: -1px;
  }
  .owner-name .first { color: var(--brand-blue); }
  .owner-name .last { color: var(--ink); }
  .services {
    position: absolute;
    left: 0; right: 0; top: 150px;
    margin: 0;
    text-align: center;
    font-size: 35px;
    line-height: 1;
  }
  .slogan-band {
    position: absolute;
    left: 10px; top: 223px;
    width: 1183px; height: 90px;
    background: var(--ink);
    color: var(--paper);
    font-size: 39px;
  }
  .slogan-band span {
    position: absolute;
    top: 25px;
    line-height: 1;
    white-space: nowrap;
  }
  .slogan-body { left: 68px; }
  .slogan-mind { left: 423px; }
  .slogan-life { left: 797px; }
  .contact-list {
    position: absolute;
    left: 0; top: 0;
    margin: 0; padding: 0;
    list-style: none;
    font-size: 32px;
  }
  .contact-item {
    position: absolute;
    left: 78px;
    height: 40px;
    width: 600px;
    white-space: nowrap;
  }
  .contact-icon {
    position: absolute;
    left: 0; top: 2px;
    width: 36px; height: 36px;
  }
  .contact-text {
    position: absolute;
    left: 68px; top: 4px;
    line-height: 1;
  }
  .contact-phone { top: 370px; }
  .contact-social-a { top: 432px; }
  .contact-email { top: 491px; }
  .contact-social-b { top: 554px; }
  .social-square {
    position: absolute;
    left: 8px; top: 7px;
    width: 26px; height: 26px;
    background: var(--ink);
  }
  .brand-mark {
    position: absolute;
    left: 725px; top: 360px;
    width: 400px; height: 260px;
  }
  .brand-dot {
    position: absolute;
    left: 118px; top: 0;
    width: 164px; height: 164px;
    border-radius: 50%;
    background: var(--brand-blue);
  }
  .brand-name {
    position: absolute;
    left: 0; right: 0; top: 178px;
    margin: 0;
    text-align: center;
    font-size: 38px;
    line-height: 1.05;
    color: var(--brand-blue);
  }
</style>
</head>
<body>
  <div class="card">
    <div class="card-edge"></div>

    <h1 class="owner-name"><span class="first">DORIEL</span><span class="last">MAXTON</span></h1>
    <p class="services">Personal Training | Bootcamps | Pilates | Nutrition</p>

    <div class="slogan-band">
      <span class="slogan-body">Healthy body</span>
      <span class="slogan-mind">Healthy mind</span>
      <span class="slogan-life">Ultimate lifestyle</span>
    </div>

    <ul class="contact-list">
      <li class="contact-item contact-phone">
        <svg class="contact-icon" viewBox="0 0 24 24" aria-hidden="true">
          <path fill="#333333" d="M6.6 10.8c1.4 2.8 3.8 5.1 6.6 6.6l2.2-2.2c.3-.3.7-.4 1-.2 1.1.4 2.3.6 3.6.6.6 0 1 .4 1 1V20c0 .6-.4 1-1 1C10.6 21 3 13.4 3 4c0-.6.4-1 1-1h3.5c.6 0 1 .4 1 1 0 1.3.2 2.5.6 3.6.1.3 0 .7-.2 1z"/>
        </svg>
        <span class="contact-text">+12 555 014 732</span>
      </li>
      <li class="contact-item contact-social-a">
        <span class="social-square" aria-hidden="true"></span>
        <span class="contact-text">KT Prime Motion</span>
      </li>
      <li class="contact-item contact-email">
        <svg class="contact-icon" viewBox="0 0 24 24" aria-hidden="true">
          <rect x="2" y="4.5" width="20" height="15" rx="1.5" fill="none" stroke="#333333" stroke-width="2.4"/>
          <path d="M3 6l9 7 9-7" fill="none" stroke="#333333" stroke-width="2.4"/>
        </svg>
        <span class="contact-text">hello@ktprimemotion.fit</span>
      </li>
      <li class="contact-item contact-social-b">
        <span class="social-square" aria-hidden="true"></span>
        <span class="contact-text">@ktprimemotion</span>
      </li>
    </ul>

    <div class="brand-mark">
      <span class="brand-dot" aria-hidden="true"></span>
      <p class="brand-name">KT PRIME<br>MOTION</p>
    </div>
  </div>
</body>
</html>
```